Chinese citizens moving to SYDNEY!

We need an A5 size flier for our new business. We would like this to be a fold-out flyer (brochure-style, i.e. 4 sides - front cover, middle, back cover). Full colour print (or 4 colour if it can be done without compromising the look). We need two versions of the same flyer - one in Chinese and one in English. Same design and imagery, just different languages. Copy is attached with imagery (subject to change once we source high res images).

Target Market(s)

Chinese citizens looking to emigrate to Sydney AND Chinese citizens who have recently moved to Sydney.

Industry/Entity Type

Business

Font styles to use
Sans Serif

Colors
ec1f27
000000
ffffff
fece3e

Requirements
Must have
• The front cover of the flier must be clean looking and show just our business name and tag line, along with an image of Sydney Harbour (provided). Main information ideally to be spread across the 2 centre pages with the back page quite clean, but if the text is too small we could consider it being spread across the remaining 3 pages (i.e. centre of the brochure, then the back cover).
• We would like it to be a clean and easy to read design. Suggested colours are written in the brief.
• It would be ideal to have a designer who can read Mandarin so that they know which characters make up a headline, which characters should not be spaced over two rows of text etc.

```html
<!DOCTYPE html>
<html lang="en">
<head>
<meta charset="utf-8">
<title>Harbourline Concierge – Brochure</title>
<link href="https://fonts.googleapis.com/css2?family=Lato:wght@400;700;900&family=Poppins:wght@500;600&display=swap" rel="stylesheet">
<style>
  :root{
    --red:#ec1f27;
    --black:#000000;
    --ink:#1e1e1e;
    --white:#ffffff;
    --charcoal:#2e2e2e;
    --backdrop:#ebe8e4;
    --swoosh-grey:#ececec;
  }
  *{margin:0;padding:0;box-sizing:border-box}
  html,body{width:1200px;height:1200px;overflow:hidden;background:var(--backdrop)}
  .spread{
    position:absolute;left:34px;top:209px;width:1332px;height:920px;
    transform:scale(0.85);transform-origin:0 0;
  }
  .page{position:absolute;top:0;width:650px;height:920px;background:var(--white);overflow:hidden}
  .page--cover{left:0}
  .page--inside{left:682px}
  .page svg.art{position:absolute;left:0;top:0}

  /* Cover */
  .brand-name{
    position:absolute;left:0;right:0;top:52px;text-align:center;
    font-family:"Poppins",sans-serif;font-weight:600;font-size:46px;color:var(--ink);
  }
  .cover-title{
    position:absolute;left:0;right:0;top:696px;text-align:center;
    font-family:"Poppins",sans-serif;font-weight:600;line-height:1.2;
  }
  .cover-title .line-one{display:block;font-size:41px;color:var(--black)}
  .cover-title .line-two{display:block;font-size:49px;color:var(--red)}
  .web-bar{
    position:absolute;left:0;top:876px;width:650px;height:37px;background:var(--charcoal);
    color:var(--white);font-family:"Lato",sans-serif;font-size:16px;letter-spacing:1.6px;
    text-align:center;line-height:37px;
  }
  .cover-edge{position:absolute;left:0;top:916px;width:650px;height:4px;background:var(--red)}

  /* Inside page */
  .intro{
    position:absolute;left:34px;top:30px;width:582px;
    font-family:"Lato",sans-serif;font-size:14px;line-height:17px;color:var(--ink);
    text-align:justify;
  }
  .intro p{margin-bottom:6px}
  .services-band{
    position:absolute;left:0;top:282px;width:650px;height:36px;background:var(--red);
    color:var(--white);font-family:"Lato",sans-serif;font-weight:900;font-size:20px;
    text-align:center;line-height:36px;letter-spacing:.3px;
  }
  .section-heading{
    position:absolute;left:0;right:0;top:330px;text-align:center;
    font-family:"Poppins",sans-serif;font-weight:600;font-size:18px;letter-spacing:2.5px;color:var(--black);
  }
  .service{
    position:absolute;display:flex;gap:10px;
    font-family:"Lato",sans-serif;font-size:14px;line-height:17px;color:var(--ink);
  }
  .service p{text-align:justify}
  .service .icon{flex:0 0 21px;width:21px;height:21px;margin-top:-1px}
  .service--left{left:32px;width:266px}
  .service--right{left:331px;width:285px}
  .service--wide{left:32px}
  .service--wide p{text-align:left;white-space:nowrap}
</style>
</head>
<body>
<div class="spread">

  <!-- Front cover -->
  <section class="page page--cover">
    <svg class="art" width="650" height="920" viewBox="0 0 650 920">
      <defs>
        <linearGradient id="harbourTones" x1="0" y1="0" x2="0" y2="1">
          <stop offset="0" stop-color="#7fb4e0"/>
          <stop offset=".45" stop-color="#b9d8ef"/>
          <stop offset=".62" stop-color="#5f93c4"/>
          <stop offset=".8" stop-color="#2f74b5"/>
          <stop offset="1" stop-color="#4a6f8f"/>
        </linearGradient>
      </defs>
      <path d="M0,150 C220,120 470,170 650,150 L650,170 C470,195 220,150 0,172 Z" fill="var(--swoosh-grey)"/>
      <g role="img" aria-label="Photograph of the harbour bridge arching over the water with the opera house and city skyline">
        <path d="M0,188 C170,165 420,205 650,238 L650,400 C520,612 260,650 0,598 Z" fill="url(#harbourTones)"/>
      </g>
      <path d="M0,175 C200,150 440,205 650,180 L650,212 C520,245 470,250 420,238 C280,205 160,185 0,205 Z" fill="var(--red)"/>
      <path d="M0,596 C270,650 520,620 650,405 L650,445 C520,650 270,680 0,628 Z" fill="var(--red)"/>
      <path d="M0,650 C280,700 540,660 650,500 L650,515 C540,680 280,718 0,668 Z" fill="var(--swoosh-grey)"/>
      <path d="M0,820 C240,860 470,840 650,800 L650,876 L0,876 Z" fill="#f6f6f6"/>
    </svg>
    <div class="brand-name">Harbourline Concierge</div>
    <h1 class="cover-title">
      <span class="line-one">Sydney’s Relocation and</span>
      <span class="line-two">Settlement Experts</span>
    </h1>
    <div class="web-bar">www.harbourlineconcierge.example.com</div>
    <div class="cover-edge"></div>
  </section>

  <!-- Page 1 -->
  <section class="page page--inside">
    <svg class="art" width="650" height="920" viewBox="0 0 650 920">
      <defs>
        <linearGradient id="schoolTones" x1="0" y1="0" x2="1" y2="1">
          <stop offset="0" stop-color="#dfe3e6"/>
          <stop offset=".5" stop-color="#8c9096"/>
          <stop offset="1" stop-color="#5b5f66"/>
        </linearGradient>
      </defs>
      <g role="img" aria-label="Photograph of smiling schoolgirls in uniform carrying tablets, with the harbour bridge in the background">
        <path d="M0,672 L322,672 C318,630 325,600 335,575 C360,560 400,548 440,545 C470,520 500,500 530,495 C580,490 630,500 650,510 L650,920 L0,920 Z" fill="url(#schoolTones)"/>
      </g>
      <path d="M0,838 C150,890 380,930 650,895 L650,920 L0,920 Z" fill="var(--red)"/>
      <path d="M0,868 C170,912 400,930 650,915 L650,920 L0,920 Z" fill="var(--white)"/>
    </svg>

    <div class="intro">
      <p>Harbourline Concierge is a premium lifestyle service supporting families who are planning or currently migrating to and investing in Australia.</p>
      <p>Specialising in the city of Sydney, Harbourline Concierge helps families to feel comfortable and at home as soon as possible.</p>
      <p>Our team of local experts provide support every step of the way – answering questions, providing advice and breaking down the language barrier.</p>
      <p>Our services are highly customisable to suit the needs of individual families. Whether it’s finding the best school for your children, the help you need in your home, knowing where to buy your favourite groceries or an introduction to a great GP or Specialist – Harbourline Concierge will cater to your every need.</p>
      <p>Your family will be assigned a professional Personal Assistant who is fluent in both English and Mandarin, making the process of migrating less daunting and more enjoyable.</p>
    </div>

    <div class="services-band">OUR SERVICES INCLUDE BUT ARE NOT LIMITED TO</div>
    <h2 class="section-heading">SCHOOL</h2>

    <div class="service service--left" style="top:372px">
      <svg class="icon" viewBox="0 0 21 21"><circle cx="10.5" cy="10.5" r="10.5" fill="var(--red)"/><path d="M5,14 H16 V10 L10.5,6 L5,10 Z" fill="none" stroke="var(--white)" stroke-width="1.4"/></svg>
      <p>Recommend the best schools and childcare centres</p>
    </div>
    <div class="service service--right" style="top:372px">
      <svg class="icon" viewBox="0 0 21 21"><circle cx="10.5" cy="10.5" r="10.5" fill="var(--red)"/><path d="M5,11 L9,14 L16,7" fill="none" stroke="var(--white)" stroke-width="2"/></svg>
      <p>Compare school rankings and academic results</p>
    </div>
    <div class="service service--left" style="top:420px">
      <svg class="icon" viewBox="0 0 21 21"><circle cx="10.5" cy="10.5" r="10.5" fill="var(--red)"/><circle cx="10.5" cy="7.5" r="2.5" fill="var(--white)"/><path d="M6,15.5 C6,11 15,11 15,15.5 Z" fill="var(--white)"/></svg>
      <p>Arrange private tours of schools and meetings with Principals</p>
    </div>
    <div class="service service--right" style="top:420px">
      <svg class="icon" viewBox="0 0 21 21"><circle cx="10.5" cy="10.5" r="10.5" fill="var(--red)"/><rect x="6" y="5" width="9" height="11" fill="none" stroke="var(--white)" stroke-width="1.4"/><path d="M8,9 H13 M8,12 H13" stroke="var(--white)" stroke-width="1.2"/></svg>
      <p>Manage the school application process through to completion</p>
    </div>
    <div class="service service--wide" style="top:468px">
      <svg class="icon" viewBox="0 0 21 21"><circle cx="10.5" cy="10.5" r="10.5" fill="var(--red)"/><path d="M5,8 H16 M5,11 H16 M5,14 H16" stroke="var(--white)" stroke-width="1.5"/></svg>
      <p>Assist with starting school, such as purchase of uniforms and textbooks,<br>understanding school procedures and more</p>
    </div>
    <div class="service service--wide" style="top:517px">
      <svg class="icon" viewBox="0 0 21 21"><circle cx="10.5" cy="10.5" r="10.5" fill="var(--red)"/><path d="M7,15 L13,6 M12,6 H15 V9" fill="none" stroke="var(--white)" stroke-width="1.5"/></svg>
      <p>Appoint private tutors to assist with learning English<br>and completing homework assignments</p>
    </div>
    <div class="service service--wide" style="top:562px">
      <svg class="icon" viewBox="0 0 21 21"><circle cx="10.5" cy="10.5" r="10.5" fill="var(--red)"/><rect x="5.5" y="6.5" width="10" height="8" fill="none" stroke="var(--white)" stroke-width="1.4"/><path d="M8,7 V14 M10.5,7 V14 M13,7 V14" stroke="var(--white)" stroke-width="1"/></svg>
      <p>Organise extra curricular activities, such as<br>piano lessons, tennis lessons and more</p>
    </div>
    <div class="service service--wide" style="top:612px">
      <svg class="icon" viewBox="0 0 21 21"><circle cx="10.5" cy="10.5" r="10.5" fill="var(--red)"/><rect x="5" y="5.5" width="6" height="6" fill="none" stroke="var(--white)" stroke-width="1.3"/><rect x="10" y="10" width="6" height="6" fill="var(--white)"/></svg>
      <p>Translate all school correspondence<br>such as academic report cards,<br>homework assignments and more</p>
    </div>
  </section>

</div>
</body>
</html>
```